A online shop for solid wood need a Stationary design

A new online shop (in Austria and Germany) for solid wood and steel furniture (feldmark-tischwerk) needs a Stationay design (letterhead, business card, envelope etc...). Dining tables, coffee tables, TV furniture and similar furniture will be sold. Everything will be custom made.

```html
<!DOCTYPE html>
<html lang="de">
<head>
<meta charset="utf-8">
<title>Feldmark Tischwerk – Visitenkarte</title>
<link rel="stylesheet" href="https://fonts.googleapis.com/css2?family=Roboto:wght@400;700;900&display=swap">
<style>
  :root {
    --backdrop: #262626;
    --card-dark: #1f1f1f;
    --card-dark-shade: #2a2a2a;
    --card-light: #f4f4f4;
    --brand-red: #e3191f;
    --text-grey: #5a5a5a;
    --rule-grey: #6d6d6d;
  }
  * { box-sizing: border-box; margin: 0; padding: 0; }
  html, body {
    width: 1200px; height: 874px; overflow: hidden;
    background: var(--backdrop);
    font-family: "Roboto", Arial, sans-serif;
  }
  .sheet { position: relative; width: 1200px; height: 874px; }
  .card {
    position: absolute; left: 290px; width: 620px; height: 354px;
    border-radius: 22px; overflow: hidden;
  }
  .card--back { top: 43px; background: var(--card-dark); }
  .card--back .shade {
    position: absolute; right: 0; top: 0; width: 46%; height: 100%;
    background: var(--card-dark-shade);
  }
  .card--front { top: 477px; background: var(--card-light); }
  .card--front .edge-band {
    position: absolute; left: 0; bottom: 0; width: 100%; height: 9px;
    background: var(--brand-red);
  }
  .wordmark {
    position: absolute; display: flex; align-items: center; gap: 14px;
    color: var(--brand-red); font-weight: 900; text-transform: uppercase;
    line-height: 1.02; letter-spacing: 2px;
  }
  .wordmark .mark-square {
    width: 38px; height: 38px; background: var(--brand-red); flex: none;
  }
  .card--back .wordmark { left: 62px; top: 128px; font-size: 34px; }
  .card--front .wordmark {
    left: 0; right: 0; top: 58px; justify-content: center; font-size: 36px;
  }
  .contact-block {
    position: absolute; left: 0; right: 0; top: 218px;
    display: flex; justify-content: center; align-items: stretch; gap: 24px;
  }
  .person { text-align: right; padding-top: 4px; }
  .person .name { color: var(--brand-red); font-weight: 700; font-size: 24px; }
  .person .role { color: var(--text-grey); font-size: 17px; margin-top: 2px; }
  .divider { width: 2px; background: var(--rule-grey); }
  .details { list-style: none; color: var(--text-grey); font-size: 16px; }
  .details li { display: flex; align-items: center; gap: 10px; height: 26px; }
  .details svg { width: 15px; height: 15px; fill: var(--brand-red); flex: none; }
</style>
</head>
<body>
<main class="sheet">
  <section class="card card--back" aria-label="Rückseite der Visitenkarte">
    <div class="shade"></div>
    <div class="wordmark"><span class="mark-square"></span><span>Feldmark<br>Tischwerk</span></div>
  </section>

  <section class="card card--front" aria-label="Vorderseite der Visitenkarte">
    <div class="wordmark"><span class="mark-square"></span><span>Feldmark<br>Tischwerk</span></div>
    <div class="contact-block">
      <div class="person">
        <p class="name">Lena Hofbauer</p>
        <p class="role">Manager</p>
      </div>
      <div class="divider"></div>
      <ul class="details">
        <li>
          <svg viewBox="0 0 16 16" aria-hidden="true"><path d="M3.5 1.5l2.5 0 1 3.5-1.6 1.2a8 8 0 0 0 4.4 4.4L11 9l3.5 1v2.5c0 1-1 2-2 2A11 11 0 0 1 1.5 3.5c0-1 1-2 2-2z"/></svg>
          <span>0660-482-7315</span>
        </li>
        <li>
          <svg viewBox="0 0 16 16" aria-hidden="true"><path d="M1 3h14v10H1z M2 4.2v.3l6 4.3 6-4.3v-.3z" fill-rule="evenodd"/></svg>
          <span>office@feldmark.at</span>
        </li>
        <li>
          <svg viewBox="0 0 16 16" aria-hidden="true"><circle cx="8" cy="8" r="7"/><path d="M1 8h14M8 1c-3 3.5-3 10.5 0 14M8 1c3 3.5 3 10.5 0 14" stroke="#f4f4f4" stroke-width="1.2" fill="none"/></svg>
          <span>www.feldmark-tischwerk.at</span>
        </li>
      </ul>
    </div>
    <div class="edge-band"></div>
  </section>
</main>
</body>
</html>
```